Website for Private Psychologist

DO NOT CONTACT ME PRIVATELY

I am a Psychologist offering psychotherapy for individuals and couples, and clinical consultation and training and education for mental and medical health professionals and agencies.

I need a redesign of my website

5 Pages (content is attached for each page)
Home
Jungian Psychotherapy
Clinical Consultation & Professional Development
Curriculum Vitae & Publications
Practice Policies and Forms

Designs can be based on these style websites
https://velmorcare.info; https://brantomind.org/; https://dorelhaskettpsychotherapy.com/

Minimalist Layout: Clean and uncluttered layout with generous white space, allowing the content and visuals to stand out'

Keep a linear, uncluttered, professional design.

Please use only royalty free images and google fonts. Please provide links to any stock images used to verify license.

private individual or couples seeking psychotherapy

Psychotherapy

5+ page

• No search feature

```html
<!DOCTYPE html>
<html lang="en">
<head>
<meta charset="utf-8">
<title>Elian Markwood — Doctor of Psychology</title>
<link rel="stylesheet" href="https://fonts.googleapis.com/css2?family=Roboto+Slab:wght@300;400;500&family=Roboto:wght@400;500&display=swap">
<style>
:root{
  --teal:#17b5c3;
  --teal-dark:#0f878d;
  --ink:#1f2326;
  --text:#4a4f54;
  --muted:#6c7177;
  --pale:#f1f1f1;
  --card:#ffffff;
  --icon-bg:#dff4f6;
  --footer:#262626;
  --footer-text:#c9c9c9;
  --slab:"Roboto Slab","Rockwell","Georgia",serif;
  --sans:"Roboto","Helvetica Neue","Arial",sans-serif;
}
*{box-sizing:border-box;margin:0;padding:0}
html,body{width:1200px;height:3452px;overflow:hidden}
body{position:relative;background:#fff;font-family:var(--sans);color:var(--text)}
.serif{font-family:var(--slab)}
.abs{position:absolute}
h1,h2,h3{font-family:var(--slab);font-weight:300;color:var(--ink)}
p{font-size:13px;line-height:21.7px}

/* header */
.site-header{position:absolute;top:0;left:0;width:1200px;height:76px;background:#fff}
.brand-name{position:absolute;left:100px;top:16px;font-family:var(--slab);font-weight:400;font-size:24px;color:var(--teal)}
.brand-sub{position:absolute;left:100px;top:50px;font-family:var(--slab);font-size:9.5px;letter-spacing:3px;color:var(--muted)}
.phone-dot{position:absolute;width:34px;height:34px;border-radius:50%;background:var(--teal);display:flex;align-items:center;justify-content:center}
.call-label{position:absolute;font-size:10px;color:var(--ink);font-family:var(--slab)}
.call-number{position:absolute;font-family:var(--slab);font-size:16px;letter-spacing:1.6px;color:var(--teal)}
.menu-icon{position:absolute;left:1064px;top:34px;width:37px}
.menu-icon span{display:block;height:2px;background:var(--ink);margin-bottom:7px}
.menu-icon span:nth-child(2){width:28px}

/* hero */
.hero-art{position:absolute;top:76px;left:0;width:1200px;height:522px;
  background:linear-gradient(100deg,#0f6a79 0%,#1690a9 28%,#3cb3d3 52%,#5cc3e2 70%,#86d2ea 100%)}
.hero-wave{position:absolute;top:520px;left:0}
.hero-title{position:absolute;left:100px;top:210px;font-size:38px;line-height:49px;color:#fff;font-weight:300}
.hero-sub{position:absolute;left:103px;top:369px;font-size:17px;line-height:29px;color:#fff}
.btn{position:absolute;background:var(--teal);color:#fff;font-family:var(--slab);font-size:18px;border-radius:24px;display:flex;align-items:center;justify-content:center}

/* intro */
.intro-art{position:absolute;left:141px;top:639px;width:376px;height:376px;border-radius:50%;
  background:linear-gradient(180deg,#4a63c9 0%,#7cb9b0 22%,#e9d9a4 36%,#fbfaf6 48%,#fbfaf6 72%,#3a4fc6 90%,#2a35b5 100%)}
.badge{position:absolute;left:385px;top:930px;width:116px;height:116px;border-radius:50%;background:var(--teal-dark);border:4px solid #fff;
  color:#fff;font-family:var(--slab);font-weight:500;font-size:15px;letter-spacing:2px;line-height:21px;text-align:center;padding-top:33px}

/* services */
.service-band{position:absolute;left:0;top:1084px;width:1200px;height:432px;background:var(--pale)}
.section-title{position:absolute;left:0;width:1200px;text-align:center;font-size:27px;line-height:37px}
.card{position:absolute;top:1328px;width:227px;height:256px;background:var(--card);border-radius:8px;box-shadow:0 6px 18px rgba(0,0,0,.07)}
.card-icon{position:absolute;left:28px;top:18px;width:56px;height:56px;border-radius:50%;background:var(--icon-bg);display:flex;align-items:center;justify-content:center}
.card h3{position:absolute;left:28px;top:90px;font-size:13px;letter-spacing:1.3px;font-weight:400;color:#333}
.card p{position:absolute;left:28px;top:118px;width:180px}
.card .arrow{position:absolute;left:28px;top:214px}

/* education */
.edu-panel{position:absolute;left:100px;top:1625px;width:1100px;height:456px;background:#fff}
.edu-art{position:absolute;left:528px;top:1696px;width:652px;height:316px;border-radius:6px;
  background:linear-gradient(90deg,#fff 0%,#fbd9cf 10%,#f6b3a2 35%,#f8c5b8 60%,#f3efec 78%,#ececec 100%)}

/* about */
.about-band{position:absolute;left:0;top:2081px;width:1200px;height:552px;background:linear-gradient(#f3f3f3,#fafafa)}
.portrait-ring{position:absolute;left:114px;top:2190px;width:354px;height:354px;border-radius:50%;border-bottom:5px solid var(--teal-dark);border-left:5px solid var(--teal-dark);transform:rotate(-10deg)}
.portrait{position:absolute;left:125px;top:2189px;width:348px;height:348px;border-radius:50%;background:linear-gradient(160deg,#8d7c70 0%,#c3a996 45%,#5a5350 100%)}

/* telehealth */
.tele-art{position:absolute;left:345px;top:2635px;width:850px;height:438px;
  background:linear-gradient(90deg,#fff 0%,#fff 30%,#f9efe0 45%,#f5c36a 60%,#e9803f 72%,#5fb6d9 85%,#3550c8 100%)}

/* footer */
.site-footer{position:absolute;left:0;top:3073px;width:1200px;height:379px;background:var(--footer)}
.foot-head{position:absolute;font-family:var(--slab);font-size:17px;color:#fff}
.foot-links{position:absolute;left:147px;top:3182px;list-style:none}
.foot-links li{font-family:var(--slab);font-size:12.5px;color:var(--footer-text);height:37px}
.social{position:absolute;top:3231px;width:22px;height:22px;border:1px solid #777;border-radius:50%}
.contact-row{position:absolute;left:868px;font-family:var(--slab);font-size:12.5px;color:var(--footer-text);display:flex;align-items:center;gap:10px}
.contact-row i{width:22px;height:22px;border-radius:50%;border:1px solid #777;display:inline-flex;align-items:center;justify-content:center}
.foot-rule{position:absolute;left:147px;top:3386px;width:943px;height:1px;background:#444}
.copyright{position:absolute;left:0;top:3413px;width:1200px;text-align:center;font-family:var(--slab);font-size:11.5px;color:var(--footer-text)}
</style>
</head>
<body>

<header class="site-header">
  <div class="brand-name">Elian Markwood</div>
  <div class="brand-sub">DOCTOR OF PSYCHOLOGY</div>
  <div class="phone-dot" style="left:841px;top:22px">
    <svg width="16" height="16" viewBox="0 0 24 24"><path fill="#fff" d="M6.6 10.8a15.1 15.1 0 0 0 6.6 6.6l2.2-2.2a1 1 0 0 1 1-.25 11.4 11.4 0 0 0 3.6.57 1 1 0 0 1 1 1V20a1 1 0 0 1-1 1A17 17 0 0 1 3 4a1 1 0 0 1 1-1h3.5a1 1 0 0 1 1 1c0 1.250.2 2.45.57 3.6a1 1 0 0 1-.25 1z"/></svg>
  </div>
  <div class="call-label" style="left:885px;top:25px">Call for a consultation:</div>
  <div class="call-number" style="left:885px;top:38px">(415) 555-0198</div>
  <div class="menu-icon"><span></span><span></span><span></span></div>
</header>

<section class="hero">
  <div class="hero-art" role="img" aria-label="Watercolour illustration of a colourful head in profile with birds flying from it against a blue sky"></div>
  <svg class="hero-wave" width="1200" height="80" viewBox="0 0 1200 80"><path d="M0 22 Q600 90 1200 20 L1200 80 L0 80Z" fill="#fff"/></svg>
  <h1 class="hero-title">Discover Healing and Growth<br>through Jungian Psychotherapy<br>&amp; Consultation</h1>
  <p class="hero-sub" style="font-size:17px;line-height:29px">Embrace Your Inner Journey with a California Licensed<br>Psychologist in San Francisco</p>
  <div class="btn" style="left:100px;top:466px;width:243px;height:46px">Book an Appointment</div>
</section>

<section class="intro">
  <div class="intro-art" role="img" aria-label="Watercolour illustration of a seated figure meditating beneath a colourful cloud"></div>
  <div class="badge">MENTAL<br>HEALTH</div>
  <h2 class="abs" style="left:581px;top:686px;font-size:27px;line-height:37px">Empowering Transformation<br>through Jungian Psychotherapy</h2>
  <p class="abs" style="left:581px;top:786px;width:415px">Unlock the potential of your mind and explore the depths of your psyche with our expert Jungian psychotherapy services. As a California Licensed Psychologist, I offer personalized and compassionate therapy for individuals and couples seeking healing and growth. Utilizing Jung's profound insights, we delve into your unconscious, dreams, and archetypes to bring profound insights and facilitate positive changes in your life.</p>
  <div class="phone-dot" style="left:581px;top:965px">
    <svg width="16" height="16" viewBox="0 0 24 24"><path fill="#fff" d="M6.6 10.8a15.1 15.1 0 0 0 6.6 6.6l2.2-2.2a1 1 0 0 1 1-.25 11.4 11.4 0 0 0 3.6.57 1 1 0 0 1 1 1V20a1 1 0 0 1-1 1A17 17 0 0 1 3 4a1 1 0 0 1 1-1h3.5a1 1 0 0 1 1 1c0 1.25.2 2.45.57 3.6a1 1 0 0 1-.25 1z"/></svg>
  </div>
  <div class="call-label" style="left:625px;top:966px">Call for a consultation:</div>
  <div class="call-number" style="left:625px;top:980px">(415) 555-0198</div>
</section>

<section class="services">
  <div class="service-band"></div>
  <h2 class="section-title" style="top:1151px">Professional Clinical<br>Consultation and Training</h2>
  <p class="abs" style="left:300px;top:1232px;width:600px;text-align:center">Unlock the potential of your mind and explore the depths of your psyche with our expert Jungian psychotherapy services.</p>

  <article class="card" style="left:100px">
    <div class="card-icon"><svg width="30" height="30" viewBox="0 0 30 30" fill="none" stroke="#2fb3bf" stroke-width="1.4"><circle cx="15" cy="15" r="10"/><circle cx="15" cy="15" r="4"/><path d="M15 5v6M15 19v6M5 15h6M19 15h6"/></svg></div>
    <h3 style="top:95px">MINDFUL INSIGHTS</h3>
    <p style="top:123px">Harness the power of mindfulness for profound self-discovery and personal growth.</p>
    <svg class="arrow" width="28" height="18" viewBox="0 0 28 18"><circle cx="12" cy="9" r="8.5" fill="#eee"/><path d="M2 9h22M20 5l4 4-4 4" fill="none" stroke="#555" stroke-width="1"/></svg>
  </article>
  <article class="card" style="left:351px">
    <div class="card-icon"><svg width="30" height="30" viewBox="0 0 30 30" fill="none" stroke="#2fb3bf" stroke-width="1.4"><path d="M15 25 5 15a5.5 5.5 0 0 1 10-6 5.5 5.5 0 0 1 10 6z"/></svg></div>
    <h3>RELATIONSHIP RENEW</h3>
    <p>Strengthen your connections and cultivate healthy relationships with expert guidance.</p>
    <svg class="arrow" width="28" height="18" viewBox="0 0 28 18"><circle cx="12" cy="9" r="8.5" fill="#eee"/><path d="M2 9h22M20 5l4 4-4 4" fill="none" stroke="#555" stroke-width="1"/></svg>
  </article>
  <article class="card" style="left:603px">
    <div class="card-icon"><svg width="30" height="30" viewBox="0 0 30 30" fill="none" stroke="#2fb3bf" stroke-width="1.4"><path d="M6 24 15 6l9 18z"/><path d="M11 16h8"/></svg></div>
    <h3>RESILIENCE BOOST</h3>
    <p>Develop inner strength and resilience to overcome life's challenges with resilience-focused support.</p>
    <svg class="arrow" width="28" height="18" viewBox="0 0 28 18"><circle cx="12" cy="9" r="8.5" fill="#eee"/><path d="M2 9h22M20 5l4 4-4 4" fill="none" stroke="#555" stroke-width="1"/></svg>
  </article>
  <article class="card" style="left:855px">
    <div class="card-icon"><svg width="30" height="30" viewBox="0 0 30 30" fill="none" stroke="#2fb3bf" stroke-width="1.4"><circle cx="15" cy="15" r="10"/><path d="M15 5a5 5 0 0 1 0 10 5 5 0 0 0 0 10"/></svg></div>
    <h3>HARMONY WITHIN</h3>
    <p>Find inner balance and harmony through therapeutic practices tailored to your unique needs.</p>
    <svg class="arrow" width="28" height="18" viewBox="0 0 28 18"><circle cx="12" cy="9" r="8.5" fill="#eee"/><path d="M2 9h22M20 5l4 4-4 4" fill="none" stroke="#555" stroke-width="1"/></svg>
  </article>
</section>

<section class="education">
  <div class="edu-panel"></div>
  <h2 class="abs" style="left:155px;top:1722px;font-size:27px;line-height:37px">Education for Mental<br>and Medical Health<br>Professionals</h2>
  <p class="abs" style="left:155px;top:1847px;width:335px">In the ever-evolving landscape of mental and medical health, ongoing education is essential. Through our educational programs, stay updated with the latest advancements and best practices in the field of Jungian psychotherapy. From workshops to seminars, we offer comprehensive training opportunities to expand your knowledge and excel in your career.</p>
  <div class="edu-art" role="img" aria-label="Collage of a brain made of coral yarn beside a seated man knitting"></div>
</section>

<section class="about">
  <div class="about-band"></div>
  <div class="portrait-ring"></div>
  <div class="portrait" role="img" aria-label="Portrait photograph of Dr. Elian Markwood"></div>
  <h2 class="abs" style="left:535px;top:2236px;font-size:27px">About Dr. Elian Markwood</h2>
  <p class="abs" style="left:535px;top:2300px;width:523px">With a passion for mental well-being and a deep understanding of Jungian psychology, I am a dedicated Psychologist committed to empowering individuals and professionals on their unique journeys. With a focus on building trust and providing a safe environment, I aim to facilitate transformative experiences that lead to lasting positive changes.</p>
  <p class="abs" style="left:535px;top:2427px;width:523px">Experience the profound impact of Jungian psychotherapy and consultation today. Book your telehealth appointment and take the first step toward a brighter and more fulfilling future. Let's embark on this transformative journey together.</p>
</section>

<section class="telehealth">
  <div class="tele-art" role="img" aria-label="Watercolour illustration of a blue figure with a rainbow cloud rising from its head"></div>
  <h2 class="abs" style="left:172px;top:2753px;font-size:27px">Telehealth Convenience</h2>
  <p class="abs" style="left:172px;top:2815px;width:485px">In today's fast-paced world, accessing mental health services should be easy and flexible. That's why all our appointments are currently available via telehealth. Embrace the convenience of virtual sessions, where you can engage in therapy or consultations from the comfort of your own space, while still receiving the same high-quality care.</p>
  <div class="btn" style="left:172px;top:2956px;width:185px;height:47px">Schedule a Call</div>
</section>

<footer class="site-footer"></footer>
<div class="foot-head" style="left:147px;top:3137px">Quick links</div>
<ul class="foot-links">
  <li>Home</li>
  <li>Jungian Psychotherapy</li>
  <li>Clinical Consultation &amp; Professional Development</li>
  <li>Curriculum Vitae &amp; Publications</li>
  <li>Practice Policies and Forms</li>
</ul>
<div class="abs serif" style="left:0;width:1200px;top:3154px;text-align:center;font-size:23px;color:#fff">Elian Markwood</div>
<div class="abs serif" style="left:0;width:1200px;top:3191px;text-align:center;font-size:11px;letter-spacing:3.5px;color:var(--footer-text)">DOCTOR OF PSYCHOLOGY</div>
<span class="social" style="left:538px"></span>
<span class="social" style="left:572px"></span>
<span class="social" style="left:605px"></span>
<span class="social" style="left:639px"></span>
<div class="foot-head" style="left:868px;top:3137px">Contact</div>
<div class="contact-row" style="top:3177px"><i><svg width="10" height="10" viewBox="0 0 24 24"><path fill="#ccc" d="M6.6 10.8a15.1 15.1 0 0 0 6.6 6.6l2.2-2.2a1 1 0 0 1 1-.25 11.4 11.4 0 0 0 3.6.57 1 1 0 0 1 1 1V20a1 1 0 0 1-1 1A17 17 0 0 1 3 4a1 1 0 0 1 1-1h3.5a1 1 0 0 1 1 1c0 1.25.2 2.45.57 3.6a1 1 0 0 1-.25 1z"/></svg></i>(415) 555-0198</div>
<div class="contact-row" style="top:3213px"><i><svg width="10" height="8" viewBox="0 0 20 16"><rect x="1" y="1" width="18" height="14" fill="none" stroke="#ccc" stroke-width="2"/><path d="M1 1l9 7 9-7" fill="none" stroke="#ccc" stroke-width="2"/></svg></i>emarkwood@quietmail.com</div>
<div class="foot-rule"></div>
<div class="copyright">© Elian Markwood 2023</div>

</body>
</html>
```